New Advertising Company Business Card

A two sided business card. One side with logo only and the other side with my information and maybe my logo again. Looking for something unique and creative, but not too busy. Info would include my name(Marcus Feldon), President, phone number, address, email address, and website. LOGO IS THE BLUE AND WHITE ONE.

Target Market(s)

CEO/VP Level Audience

Industry/Entity Type

Business

Contact Information for Business Card

In Description.

```html
<!DOCTYPE html>
<html lang="en">
<head>
<meta charset="utf-8">
<title>Kestrel Advertising – Business Card</title>
<link rel="stylesheet" href="https://fonts.googleapis.com/css2?family=Montserrat:wght@400;500;700&display=swap">
<style>
  :root {
    --stage: #1c1c1d;
    --card-light: #ffffff;
    --card-dark: #2a2a2b;
    --brand-blue: #2b7fc7;
    --ink: #3a3a3c;
    --ink-soft: #5a5a5e;
    --white: #ffffff;
  }
  * { box-sizing: border-box; margin: 0; padding: 0; }
  html, body { width: 1200px; height: 900px; overflow: hidden; }
  body {
    background: var(--stage);
    font-family: "Montserrat", sans-serif;
    display: flex;
    flex-direction: column;
    align-items: center;
    justify-content: center;
    gap: 60px;
  }
  .card {
    width: 560px;
    height: 320px;
    position: relative;
    box-shadow: 0 10px 30px rgba(0,0,0,.45);
  }
  .card--front { background: var(--card-light); }
  .card--back { background: var(--card-dark); }

  .wordmark {
    font-weight: 700;
    color: var(--brand-blue);
    text-transform: uppercase;
    letter-spacing: .06em;
    line-height: 1.15;
    display: flex;
    align-items: center;
    gap: 12px;
  }
  .wordmark__dot {
    width: 14px; height: 14px;
    border-radius: 50%;
    background: var(--brand-blue);
    flex: none;
  }
  .card--front .wordmark {
    position: absolute;
    left: 44px; top: 128px;
    font-size: 22px;
  }

  .contact {
    position: absolute;
    left: 296px; top: 88px; right: 0;
  }
  .contact__name {
    font-size: 22px;
    font-weight: 700;
    color: var(--brand-blue);
    text-transform: uppercase;
    letter-spacing: .01em;
  }
  .contact__title {
    font-size: 12px;
    font-weight: 500;
    color: var(--ink);
    text-transform: uppercase;
    letter-spacing: .05em;
    margin-top: 2px;
  }
  .contact__rule {
    height: 1px;
    background: var(--brand-blue);
    margin: 12px 0 14px;
  }
  .contact__address {
    font-size: 11px;
    color: var(--ink-soft);
    line-height: 1.5;
    margin-bottom: 10px;
  }
  .contact__list { list-style: none; }
  .contact__item {
    display: flex;
    align-items: center;
    gap: 10px;
    font-size: 11px;
    color: var(--ink-soft);
    line-height: 1.75;
  }
  .contact__icon { width: 11px; height: 11px; flex: none; }

  .card--back .wordmark {
    position: absolute;
    left: 0; right: 0; top: 128px;
    justify-content: center;
    font-size: 28px;
  }
  .card--back .website {
    position: absolute;
    left: 0; right: 0; bottom: 44px;
    text-align: center;
    font-size: 13px;
    font-weight: 500;
    color: var(--white);
    letter-spacing: .04em;
  }
</style>
</head>
<body>

  <section class="card card--front" aria-label="Business card front">
    <div class="wordmark"><span class="wordmark__dot"></span><span>Kestrel<br>Advertising</span></div>

    <div class="contact">
      <p class="contact__name">Marcus Feldon</p>
      <p class="contact__title">President</p>
      <div class="contact__rule"></div>
      <p class="contact__address">Unit 12, The Harlow Works,<br>Redbourn, Herts AL9 4QP</p>
      <ul class="contact__list">
        <li class="contact__item">
          <svg class="contact__icon" viewBox="0 0 12 12" fill="none" stroke="#2b7fc7" stroke-width="1.2"><rect x="3" y="0.8" width="6" height="10.4" rx="1"/><line x1="5.2" y1="9.4" x2="6.8" y2="9.4"/></svg>
          +63 917 555 0142
        </li>
        <li class="contact__item">
          <svg class="contact__icon" viewBox="0 0 12 12" fill="none" stroke="#2b7fc7" stroke-width="1.2"><rect x="0.8" y="2.5" width="10.4" height="7" rx=".6"/><polyline points="0.8,2.8 6,6.6 11.2,2.8"/></svg>
          info@kestrelads.com
        </li>
        <li class="contact__item">
          <svg class="contact__icon" viewBox="0 0 12 12" fill="none" stroke="#2b7fc7" stroke-width="1.1"><circle cx="6" cy="6" r="5"/><ellipse cx="6" cy="6" rx="2.2" ry="5"/><line x1="1" y1="6" x2="11" y2="6"/></svg>
          www.kestrelads.com
        </li>
      </ul>
    </div>
  </section>

  <section class="card card--back" aria-label="Business card back">
    <div class="wordmark"><span class="wordmark__dot"></span><span>Kestrel<br>Advertising</span></div>
    <p class="website">www.kestrelads.com</p>
  </section>

</body>
</html>
```